Enhance the web site presence of Kolrith Global Limited

Upgrade the current web site www.kolrithpanel.com to share with the audience our current plan and future developments of our company. I have created a worksheet which shows all the pages that I like to have. The home page in English, Japanese and Chinese is hyperlinked to the various pages. Under the product, we should allow the user to select "single sided PCB or double sided PCB". The translation of the contents of the pages with Japanese is not complete but the English and Chinese are complete. You can download the briefing and photos in the dropbox files below;

https://www.sharelocker.net/sh/xk4trw92mpd3ab1/BBQm_Lp841zzPq2Rw7KtYnHjEa?dl=0

Target Market(s)

Electronic companies

Industry/Entity Type

Electronic

Coding

Coded - Design and coding required

Number of Pages Required

5+ page

Font styles to use
Sans Serif

Colors
00a990
0353a1
33b8a4

Requirements
Must have
• Get a sense of confidence on our company's integrity and capability to deliver the highest quality PCBs with the most competitive prices and best services. A sense of elegance is essential as we DON'T treat profits as the number one goal. Our number goal is to do the RIGHT things right. Having a mixture of our company photos will be appropriate.

```html
<!DOCTYPE html>
<html lang="en">
<head>
<meta charset="utf-8">
<title>Our Facilities – Kolrith Global Limited</title>
<link href="https://fonts.googleapis.com/css2?family=Poppins:wght@500;600&family=Roboto:wght@400;500;700&display=swap" rel="stylesheet">
<style>
:root{
  --blue:#0353a1;
  --blue-dark:#07468c;
  --teal:#33b8a4;
  --green:#00a990;
  --ink:#222;
  --text:#555;
  --white:#fff;
}
*{margin:0;padding:0;box-sizing:border-box}
html,body{width:900px;height:1200px;overflow:hidden;background:var(--white);font-family:'Roboto',sans-serif;color:var(--ink)}
.page{position:relative;width:900px;height:1200px}

.topbar{position:absolute;left:0;top:0;width:900px;height:31px;background:var(--blue);color:var(--white);font-size:10px}
.topbar .contact{position:absolute;left:67px;top:10px;display:flex;gap:16px;align-items:center}
.topbar .contact span{display:flex;align-items:center;gap:5px}
.topbar .lang{position:absolute;left:716px;top:12px;font-size:8px;display:flex;align-items:center;gap:4px}
.flag{width:12px;height:8px;background:#c8102e;border:2px solid #1b3f8f}
.login-tab{position:absolute;left:748px;top:0}
.login-tab .label{position:absolute;left:38px;top:12px;font-size:8px;display:flex;align-items:center;gap:4px;white-space:nowrap}

.navbar{position:absolute;left:0;top:31px;width:900px;height:70px;background:var(--white)}
.brand{position:absolute;left:67px;top:21px;display:flex;align-items:center;gap:6px;font-family:'Roboto',sans-serif;font-weight:700;font-size:22px;color:var(--blue)}
.brand .mark{width:12px;height:12px;background:var(--green)}
.menu{position:absolute;top:30px;left:0;width:900px;list-style:none;font-size:10px;font-weight:500;color:#333}
.menu li{position:absolute;white-space:nowrap}
.menu .active{color:var(--teal)}
.menu .active::before{content:"";position:absolute;left:-7px;top:-30px;width:79px;height:2px;background:var(--teal)}

.hero{position:absolute;left:0;top:101px;width:900px;height:340px;overflow:hidden}
.hero-photo{position:absolute;inset:0;background:linear-gradient(120deg,#2e3d36 0%,#3f4f46 35%,#25405a 70%,#1f3560 100%)}
.hero h1{position:absolute;top:90px;width:900px;text-align:center;font-family:'Poppins',sans-serif;font-weight:600;font-size:26px;color:var(--white)}
.hero .crumbs{position:absolute;top:123px;width:900px;text-align:center;font-size:10px;color:var(--white);font-weight:500}
.hero svg{position:absolute;left:0;top:0}

.gallery .accent{position:absolute;left:76px;top:582px;width:60px;height:129px;background:var(--teal);border-radius:6px}
.gallery .photo-main{position:absolute;left:126px;top:471px;width:236px;height:333px;border-radius:12px;background:linear-gradient(160deg,#f3f1e8,#dcdcd4 55%,#c9ccc6);box-shadow:0 8px 24px rgba(0,0,0,.12)}
.gallery .frame{position:absolute;left:250px;top:638px;width:140px;height:200px;background:var(--white);border-radius:8px 0 0 0}
.gallery .photo-small{position:absolute;left:261px;top:650px;width:123px;height:173px;border-radius:6px;background:linear-gradient(170deg,#e8e6dc,#cfd8cf 50%,#b9c3bb)}

.intro{position:absolute;left:424px;top:537px;width:364px}
.intro h2{font-family:'Poppins',sans-serif;font-weight:500;font-size:21px;color:var(--ink);margin-bottom:10px;margin-left:0}
.intro p{font-size:11.4px;line-height:19.4px;color:var(--text);text-align:justify;margin-left:2px;margin-bottom:12px}

.footer{position:absolute;left:0;top:919px;width:900px;height:281px;background:var(--blue);color:var(--white)}
.footer .map{position:absolute;left:605px;top:90px;width:215px;height:120px;border-radius:40%;background:radial-gradient(ellipse,rgba(255,255,255,.09),rgba(255,255,255,0) 70%)}
.footer .brand-foot{position:absolute;left:0;top:112px;width:392px;text-align:center;font-weight:700;font-size:24px;letter-spacing:.5px}
.footer .copy{position:absolute;left:0;top:156px;width:392px;text-align:center;font-size:10.4px;line-height:15.5px;font-weight:500}
.footer h3{font-size:13.5px;font-weight:700;margin-bottom:6px}
.links{position:absolute;left:400px;top:67px}
.links ul{list-style:none;font-size:9.6px;font-weight:500}
.links li{height:20.3px;display:flex;align-items:center;gap:6px}
.links li::before{content:"›";font-size:9px;opacity:.8}
.contacts{position:absolute;left:632px;top:67px}
.contacts ul{list-style:none;font-size:9.6px;font-weight:500}
.contacts li{height:20.3px;display:flex;align-items:center;gap:4px}
.contacts li.indent{padding-left:12px}
.contacts svg{width:8px;height:8px}
.to-top{position:absolute;left:846px;top:1143px;width:25px;height:25px;border-radius:50%;background:var(--teal)}
</style>
</head>
<body>
<div class="page">

  <header class="topbar">
    <div class="contact">
      <span><svg width="9" height="7" viewBox="0 0 9 7"><rect x=".5" y=".5" width="8" height="6" fill="none" stroke="#fff"/><path d="M.5 .5 4.5 4 8.5 .5" fill="none" stroke="#fff"/></svg>sales@kolrithpanel.com</span>
      <span><svg width="8" height="8" viewBox="0 0 24 24"><path fill="#fff" d="M6.6 10.8a15 15 0 0 0 6.6 6.6l2.2-2.2c.3-.3.7-.4 1-.2 1.1.4 2.3.6 3.6.6.6 0 1 .4 1 1V20c0 .6-.4 1-1 1A17 17 0 0 1 3 4c0-.6.4-1 1-1h3.5c.6 0 1 .4 1 1 0 1.3.2 2.5.6 3.6.1.3 0 .7-.2 1z"/></svg>(852) 2740 5196</span>
    </div>
    <div class="lang"><span class="flag"></span>EN ⌄</div>
    <div class="login-tab">
      <svg width="112" height="35" viewBox="0 0 112 35"><path d="M0 0 Q20 0 26 22 Q30 34 40 34 H78 Q86 34 92 20 Q100 0 112 0 Z" fill="#33b8a4"/></svg>
      <span class="label"><svg width="7" height="8" viewBox="0 0 7 8"><rect y="3.5" width="7" height="4.5" fill="#fff"/><path d="M1.5 3.5V2a2 2 0 0 1 4 0v1.5" fill="none" stroke="#fff"/></svg>LOGIN</span>
    </div>
  </header>

  <nav class="navbar">
    <div class="brand"><span class="mark"></span>Kolrith</div>
    <ul class="menu">
      <li style="left:343px">HOME</li>
      <li style="left:400px">PRODUCTS</li>
      <li class="active" style="left:478px">OUR FACILITIES</li>
      <li style="left:576px">CUSTOMER</li>
      <li style="left:656px">NEWS</li>
      <li style="left:712px">QUOTES</li>
      <li style="left:778px">CONTACT US</li>
    </ul>
  </nav>

  <section class="hero">
    <div class="hero-photo" role="img" aria-label="Factory floor with automated PCB production machinery"></div>
    <h1>Our Facilities</h1>
    <div class="crumbs">Home / Facilities</div>
    <svg width="900" height="340" viewBox="0 0 900 340">
      <path d="M0 296 C200 225 450 190 700 181 L700 190 C420 210 200 260 0 340 Z" fill="#33b8a4"/>
      <path d="M0 340 C150 255 330 210 460 209 C640 209 790 222 900 243 L900 340 Z" fill="#fff"/>
    </svg>
  </section>

  <section class="gallery">
    <div class="accent"></div>
    <div class="photo-main" role="img" aria-label="Automated optical inspection machine in the factory"></div>
    <div class="frame"></div>
    <div class="photo-small" role="img" aria-label="Board handling equipment with stacked panels"></div>
  </section>

  <section class="intro">
    <h2>Our investment and upgrade</h2>
    <p>Maintaining a highly automated factory is the only way to ensure consistent product and long term competitive efficiency.</p>
    <p>From 2015 to 2017, Kolrith invested over US$3.5 million in automating our production and quality control process and enhancing our environmental processing facility. We will spend a further US$1.5 million in 2018 to continue our improvement process to ensure we are one of the most efficient and highest quality single sided PCB manufacturers in Asia. By the end of 2018, 100% of our PCBs will be inspected by AVI before they are delivered to our customers.</p>
  </section>

  <footer class="footer">
    <div class="map" role="img" aria-label="Faint dotted world map"></div>
    <div class="brand-foot">Kolrith</div>
    <div class="copy">Copyright © 2018, Kolrith Global Limited.<br>All Rights Reserved</div>
    <div class="links">
      <h3>USEFUL LINKS</h3>
      <ul>
        <li>Home</li><li>Products</li><li>Our Facilities</li><li>Customer</li><li>News</li><li>Quotes</li><li>Contact Us</li>
      </ul>
    </div>
    <div class="contacts">
      <h3>CONTACT US</h3>
      <ul>
        <li><svg viewBox="0 0 24 24"><path fill="#fff" d="M12 2a7 7 0 0 0-7 7c0 5 7 13 7 13s7-8 7-13a7 7 0 0 0-7-7zm0 9.5A2.5 2.5 0 1 1 12 6.5a2.5 2.5 0 0 1 0 5z"/></svg>Kolrith Global Limited</li>
        <li class="indent">28/F Harbour Crest</li>
        <li class="indent">71 Marlow Road</li>
        <li class="indent">Wan Chai, HONG KONG</li>
        <li><svg viewBox="0 0 24 24"><path fill="#fff" d="M6.6 10.8a15 15 0 0 0 6.6 6.6l2.2-2.2c.3-.3.7-.4 1-.2 1.1.4 2.3.6 3.6.6.6 0 1 .4 1 1V20c0 .6-.4 1-1 1A17 17 0 0 1 3 4c0-.6.4-1 1-1h3.5c.6 0 1 .4 1 1 0 1.3.2 2.5.6 3.6.1.3 0 .7-.2 1z"/></svg>Telephone: (852)27405196</li>
        <li><svg viewBox="0 0 24 24"><path fill="#fff" d="M6 3h12v5H6zM3 9h18v8h-3v4H6v-4H3zm5 6v4h8v-4z"/></svg>Fax: (852)27405197</li>
        <li><svg viewBox="0 0 24 24"><path fill="#fff" d="M2 5h20v14H2zm2 2v.5l8 5 8-5V7z"/></svg>Email: Sales@kolrithpanel.com</li>
      </ul>
    </div>
    <svg class="to-top" style="position:absolute;left:846px;top:224px" width="25" height="25" viewBox="0 0 25 25"><circle cx="12.5" cy="12.5" r="12.5" fill="#33b8a4"/><path d="M9.5 14 12.5 11 15.5 14" fill="none" stroke="#fff" stroke-width="1.4"/></svg>
  </footer>

</div>
</body>
</html>
```